Bramblewick Gardening Services. A6 flyer single sided

Need an A6 flyer designing. Single sided.
I am a gardener.
I do lawn mowing - one-off garden tidy ups or regular fortnightly visits.
All kinds of trees expertly felled, topped or pruned.
Hedge cutting.
Fencing replaced or repaired.
Fully insured.
Access to fully qualified and licenced tree arborist
07724 316048 or 01632 742918.

I have attached my business card and letter head logo.
I'm open to new designs without incorporating any of my artwork.

Industry/Entity Type

Gardener

```html
<!DOCTYPE html>
<html lang="en">
<head>
<meta charset="utf-8">
<title>Bramblewick Gardening Services – A6 Flyer</title>
<link rel="stylesheet" href="https://fonts.googleapis.com/css2?family=Montserrat:wght@500;600;700&display=swap">
<style>
  :root {
    --ink-green: #1b4a3a;
    --row-green: #194a3b;
    --band-dark: #15543d;
    --band-light: #2aa172;
    --grass-dark: #1f5a1c;
    --grass-mid: #3d8a2a;
    --grass-light: #4f9c33;
    --paper: #ffffff;
    --paper-shade: #e9ecea;
    --type: "Montserrat", "Century Gothic", sans-serif;
  }
  * { margin: 0; padding: 0; box-sizing: border-box; }
  html, body { width: 851px; height: 1200px; overflow: hidden; background: #fff; }
  .flyer {
    position: relative;
    width: 851px;
    height: 1200px;
    overflow: hidden;
    font-family: var(--type);
  }
  .header {
    position: absolute;
    left: 0; top: 0;
    width: 851px; height: 290px;
    background: linear-gradient(180deg, var(--paper) 0%, var(--paper) 40%, var(--paper-shade) 100%);
  }
  .brand-name {
    position: absolute;
    left: 0; top: 95px;
    width: 851px;
    text-align: center;
    font-weight: 600;
    font-size: 100px;
    line-height: 1;
    letter-spacing: 1px;
    color: var(--ink-green);
  }
  .lawn {
    position: absolute;
    left: 0; top: 290px;
    width: 851px; height: 910px;
    background:
      radial-gradient(ellipse at 50% 45%, var(--grass-light) 0%, var(--grass-mid) 45%, var(--grass-dark) 100%);
  }
  .service-band {
    position: absolute;
    left: 0; top: 281px;
    width: 851px; height: 73px;
    background: linear-gradient(90deg, var(--band-dark) 0%, var(--band-light) 50%, var(--band-dark) 100%);
    box-shadow: 0 3px 8px rgba(0,0,0,0.35);
    color: var(--paper);
    font-weight: 600;
    font-size: 51px;
    line-height: 73px;
    text-align: center;
    letter-spacing: 0.5px;
  }
  .services {
    position: absolute;
    left: 144px; top: 360px;
    width: 563px; height: 649px;
    background: var(--paper);
    list-style: none;
    padding-top: 34px;
  }
  .service {
    height: 59px;
    margin-bottom: 9.6px;
    background: var(--row-green);
    color: var(--paper);
    font-weight: 600;
    font-size: 38px;
    line-height: 59px;
    text-align: center;
    white-space: nowrap;
  }
  .service--note {
    background: var(--paper);
    color: var(--ink-green);
    margin-bottom: 0;
  }
  .contact {
    position: absolute;
    left: 0; top: 1012px;
    width: 851px;
    text-align: center;
    color: var(--paper);
    font-weight: 600;
  }
  .contact-name { font-size: 37px; line-height: 46px; }
  .contact-phones { font-size: 39px; line-height: 56px; letter-spacing: 0.5px; }
  .contact-email { font-size: 31px; line-height: 44px; }
</style>
</head>
<body>
  <main class="flyer">
    <header class="header">
      <h1 class="brand-name">BRAMBLEWICK</h1>
    </header>
    <div class="lawn" role="img" aria-label="Close-up photograph of lush green lawn grass"></div>
    <h2 class="service-band">GARDENING SERVICES</h2>
    <ul class="services">
      <li class="service">LAWN MOWING</li>
      <li class="service">GARDEN TIDY UPS</li>
      <li class="service">FORTNIGHTLY VISITS</li>
      <li class="service">TREE FELLING</li>
      <li class="service">TOPPING &amp; PRUNING</li>
      <li class="service">HEDGE CUTTING</li>
      <li class="service">FENCING REPAIRS</li>
      <li class="service">ARBORIST ACCESS</li>
      <li class="service service--note">FULLY INSURED</li>
    </ul>
    <footer class="contact">
      <p class="contact-name">ROB FENNIMORE</p>
      <p class="contact-phones">07724 316048 • 01632 742918</p>
      <p class="contact-email">BRAMBLEWICK@FERNPOST.COM</p>
    </footer>
  </main>
</body>
</html>
```